Web Design Project

I need a web site for and medical spa aesthetics
We offer plumavex softaquin and laser photo facials
http://www.briefnook-example.com/design/4817306
Cosmetic Treatments
- Nervela/Calmira
- Fillers
- Liquid Face Lift
- Skin Tightening
- Skin Complexion Analysis
- Anti-Aging Treatments
- Wrinkle Reduction
- Sclerotherapy- Leg Veins
Laser & Pulsed Light
- Brown Age Spot Removal
- Painless Laser Hair Removal
- Laser Skin Resurfacing
- Facial Redness Reduction
- Tattoo Removal
Target Market(s)
My target market is women over 40 as well as men over 50
Industry/Entity Type
Medical
Requirements
Must have
- Pleasuring to the eye for both males and females
The name of the spa us glowhaven aesthetics and laser
Nice to have
- Should be also viewable on mobile Tavix kestrine etc
And should have scheduling calendar
Should not have
- Needs to be beautiful and elegant no leaves or flowers like
Every other site

```html
<!DOCTYPE html>
<html lang="en">
<head>
<meta charset="utf-8">
<title>Glowhaven Aesthetics and Laser</title>
<link rel="stylesheet" href="https://fonts.googleapis.com/css2?family=Comfortaa:wght@300;400&family=Oswald:wght@300&family=PT+Sans+Narrow:wght@400;700&display=swap">
<style>
:root{
  --orange:#e8501a;
  --blue:#5470a8;
  --blue-text:#c9d5ef;
  --blue-title:#dbe4f7;
  --slate:#4b6aa5;
  --grey-panel:#5f5f5f;
  --field:#ececec;
  --label:#dedede;
  --ink:#333;
  --muted:#777;
  --white:#fff;
}
*{margin:0;padding:0;box-sizing:border-box}
html,body{width:896px;height:1200px;overflow:hidden;background:var(--white)}
body{position:relative;font-family:"PT Sans Narrow",sans-serif;color:var(--ink)}
.brand{position:absolute;left:27px;top:30px;display:flex;align-items:center;gap:8px;color:var(--slate)}
.brand-dot{width:22px;height:22px;border-radius:50%;background:var(--orange);flex:none}
.brand-name{font-family:"Comfortaa",sans-serif;font-weight:400;font-size:15px;line-height:1.25;letter-spacing:.5px;text-transform:uppercase}
.contact{position:absolute;right:11px;top:4px;text-align:right}
.call{font-family:"Oswald",sans-serif;font-weight:300;font-size:30px;color:#8a8a8a;letter-spacing:-.5px}
.call span{color:var(--slate);font-size:27px;margin-right:10px}
.address{font-size:12px;color:var(--muted);margin-top:-2px}
.main-nav{position:absolute;left:203px;top:66px;width:693px;height:32px;background:var(--orange)}
.main-nav a{position:absolute;top:0;height:32px;line-height:32px;font-family:"Comfortaa",sans-serif;font-weight:300;font-size:17px;letter-spacing:-.3px;color:var(--white);text-decoration:none;white-space:nowrap}
.main-nav .sep{position:absolute;top:16px;width:1px;height:13px;background:#f6c6b2}
.hero{position:absolute;left:0;top:98px;width:535px;height:252px;background:linear-gradient(100deg,#f2eee9 0%,#e6c9ad 40%,#d9ad86 60%,#f1ebe6 100%)}
.intro{position:absolute;left:0;top:350px;width:535px;height:625px;background:var(--blue);color:var(--white)}
.intro h1{position:absolute;left:18px;top:22px;font-family:"Comfortaa",sans-serif;font-weight:300;font-size:32px;letter-spacing:-1.5px;white-space:nowrap}
.intro .copy{position:absolute;left:20px;top:90px;width:478px;font-size:12px;line-height:15.5px}
.intro .copy p+p{margin-top:15px}
.intro h2{position:absolute;left:18px;top:276px;font-family:"Comfortaa",sans-serif;font-weight:300;font-size:29px;letter-spacing:-.5px}
.service{position:absolute;width:240px}
.service h3{font-family:"PT Sans Narrow",sans-serif;font-weight:400;font-size:21px;color:var(--blue-title);position:relative;padding-left:18px}
.service h3::before{content:"";position:absolute;left:3px;top:11px;width:6px;height:6px;border-radius:50%;background:var(--blue-title)}
.service ul{list-style:none;padding-left:18px;margin-top:6px}
.service li{font-size:11.5px;line-height:15.5px;color:var(--blue-text)}
.gallery{position:absolute;left:0;top:0}
.portrait{position:absolute;width:162px;height:162px;border-radius:50%;border:2px solid var(--orange);background:radial-gradient(circle at 45% 40%,#f1d6c2,#c99a7a 80%)}
.appointment{position:absolute;left:549px;top:665px;width:335px;height:310px;background:var(--grey-panel)}
.appointment h4{position:absolute;left:41px;top:6px;font-family:"Comfortaa",sans-serif;font-weight:400;font-size:18px;color:var(--white);letter-spacing:-.3px}
.field-label{position:absolute;left:41px;font-weight:700;font-size:14.5px;color:var(--label)}
.field{position:absolute;left:40px;width:259px;height:21px;background:var(--field)}
.site-footer{position:absolute;left:14px;top:992px;font-family:Arial,sans-serif;font-size:11.5px;color:var(--ink)}
.site-footer span{margin:0 8px;color:#999}
.copyright{position:absolute;right:11px;top:986px;font-family:"Comfortaa",sans-serif;font-size:9.5px;color:var(--ink)}
</style>
</head>
<body>
<header>
  <div class="brand"><span class="brand-dot"></span><div class="brand-name">Glowhaven<br>aesthetics and laser</div></div>
  <div class="contact">
    <div class="call"><span>call us</span>555-014-7392</div>
    <div class="address">Address, City, State/Province Zip Cod</div>
  </div>
  <nav class="main-nav">
    <a href="#" style="left:16px">home</a><i class="sep" style="left:78px"></i>
    <a href="#" style="left:110px">about us</a><i class="sep" style="left:215px"></i>
    <a href="#" style="left:236px">services</a><i class="sep" style="left:330px"></i>
    <a href="#" style="left:352px">feedbacks</a><i class="sep" style="left:467px"></i>
    <a href="#" style="left:493px">contact us</a>
  </nav>
</header>

<div class="hero" role="img" aria-label="Photo of a relaxed woman with bare shoulders during a spa treatment"></div>

<section class="intro">
  <h1>Welcome to GLOWHAVEN</h1>
  <div class="copy">
    <p>Our mission is to help patients live healthier lives. We provide a caring, nurturing environment where your comfort and health is of primary importance. The members of our team utilize the latest technologies to deliver the highest quality care.</p>
    <p>To be board certified in Plastic Surgery, it requires that you graduate from an accredited medical school, complete at least 5 years of hospital based surgical residency, followed by a minimum of 2 years of plastic surgery fellowship and pass comprehensive oral and written exams. Last Name(s) manages a wide variety of problems relating to the face and body. He practices a full scope of plastic surgery with expertise in Cosmetic and Reconstructive surgery.</p>
  </div>
  <h2>our services</h2>
  <div class="service" style="left:23px;top:316px">
    <h3>Cosmetic Treatments</h3>
    <ul><li>Nervela/Calmira</li><li>Fillers</li><li>Liquid Face Lift</li><li>Skin Tightening</li><li>Skin Complexion Analysis</li><li>Anti-Aging Treatments</li><li>Wrinkle Reduction</li><li>Sclerotherapy- Leg Veins</li></ul>
  </div>
  <div class="service" style="left:288px;top:316px">
    <h3>Laser &amp; Pulsed Light</h3>
    <ul><li>Brown Age Spot Removal</li><li>Painless Laser Hair Removal</li><li>Laser Skin Resurfacing</li><li>Facial Redness Reduction</li><li>Tattoo Removal</li></ul>
  </div>
  <div class="service" style="left:23px;top:491px">
    <h3>Skin Care, Face &amp; Beauty</h3>
    <ul><li>Beauty Services</li><li>Peels</li><li>Facials</li><li>Dermaplaning</li><li>MicroDermabrasion</li><li>Eyelash Thickening &amp; Lengthening</li></ul>
  </div>
  <div class="service" style="left:288px;top:491px">
    <h3>Body Treatments</h3>
    <ul><li>Cryocontour</li><li>Waxing</li><li>Massage</li><li>Body Treatments</li></ul>
  </div>
</section>

<div class="gallery">
  <div class="portrait" style="left:545px;top:109px" role="img" aria-label="Smiling man shading his eyes"></div>
  <div class="portrait" style="left:723px;top:109px" role="img" aria-label="Woman with clear skin touching her chin"></div>
  <div class="portrait" style="left:545px;top:292px" role="img" aria-label="Man receiving a shoulder massage"></div>
  <div class="portrait" style="left:723px;top:292px" role="img" aria-label="Eyebrow shaping treatment"></div>
  <div class="portrait" style="left:545px;top:483px;background:radial-gradient(circle at 50% 45%,#d8b49a,#6f6a66 80%)" role="img" aria-label="Man receiving a facial mask"></div>
  <div class="portrait" style="left:723px;top:483px;background:radial-gradient(circle at 55% 45%,#f3dccc,#d8eef5 85%)" role="img" aria-label="Woman receiving a filler injection"></div>
</div>

<form class="appointment">
  <h4>set an appointment</h4>
  <label class="field-label" style="top:36px">name</label><div class="field" style="top:56px"></div>
  <label class="field-label" style="top:82px">email</label><div class="field" style="top:102px"></div>
  <label class="field-label" style="top:128px">phone</label><div class="field" style="top:148px"></div>
  <label class="field-label" style="top:183px">comments</label><div class="field" style="top:202px;height:95px"></div>
</form>

<footer>
  <nav class="site-footer">HOME<span>·</span>ABOUT US<span>·</span>SERVICES<span>·</span>FEEDBCKS<span>·</span>CONTACT US</nav>
  <div class="copyright">© Copyright 2013 BRIGHTWELL VENTURES All Rights Reserved.</div>
</footer>
</body>
</html>
```